Medical Billing Company needs Trifold Brochure Design

We do medical billing and consulting for all types of medical services including hospitals, clinics, physical therapy, mental health, and all other physician specialties. We want to attract new clients from all areas. This is what we have listed on our LinkedIn page: Korvath Billing and Consulting offers 128 years of combined medical billing, coding, credentialing, auditing, and practice management experience. Integrity, reliability, dedication, and open communication are the cornerstones of our foundation. We strive to create meaningful relationships with our clients so they may focus on what they do best, and allow us to handle the rest.

We understand the changes occurring in our healthcare system. Reimbursement is decreasing, expenses are increasing, and the dedication and tenacity to collect every dollar due from the carriers is vital to the financial health of the hospital or practitioner.

Target Market(s)

Physicians, hospitals and any other providers in the medical field such as durable medical equipment suppliers and mid-level providers

Font styles to use
Sans Serif

Colors

Designer to choose colors to be used in the design.

Requirements
Must have
• Specifics list of services we offer. List attached.

```html
<!DOCTYPE html>
<html lang="en">
<head>
<meta charset="utf-8">
<title>Korvath Billing and Consulting – Trifold Brochure</title>
<link href="https://fonts.googleapis.com/css2?family=Open+Sans:ital,wght@0,400;0,600;0,700;1,400&display=swap" rel="stylesheet">
<style>
  :root {
    --navy: #1a5d8f;
    --sky: #4fc3e8;
    --green: #3db54a;
    --ink: #4a4a4a;
    --rule: #9fd8ec;
    --paper: #ffffff;
    --backdrop: #e4e6e8;
    --quote-bg: #eeeeee;
  }
  * { box-sizing: border-box; margin: 0; padding: 0; }
  html, body { width: 1200px; height: 1200px; overflow: hidden; }
  body { background: var(--backdrop); font-family: "Open Sans", sans-serif; color: var(--ink); position: relative; }

  .sheet { position: absolute; background: var(--paper); overflow: hidden; }
  .inside { left: 65px; top: 53px; width: 697px; height: 541px; }
  .outside { left: 414px; top: 626px; width: 699px; height: 541px; }

  .block { position: absolute; }
  .photo { position: absolute; }

  /* inside spread */
  .intro-panel { left: 0; top: 0; width: 465px; height: 240px; background: var(--navy); color: #fff; }
  .intro-title { position: absolute; left: 34px; top: 32px; font-weight: 700; font-size: 16px; letter-spacing: .2px; }
  .intro-sub { position: absolute; left: 36px; top: 77px; width: 200px; font-weight: 700; font-size: 14px; line-height: 15.5px; color: var(--sky); }
  .intro-body { position: absolute; left: 36px; top: 145px; width: 178px; font-size: 9.3px; line-height: 15.7px; text-align: justify; color: #e6f1f8; }
  .intro-body.right { left: 263px; top: 70px; width: 173px; }
  .notice-band { left: 0; top: 240px; width: 465px; height: 62px; background: var(--sky); color: #163a55; font-size: 9.2px; line-height: 12.2px; padding: 14px 30px 0 39px; }
  .team-photo { left: 0; top: 302px; width: 465px; height: 239px; background: linear-gradient(135deg, #f3f3f1 0%, #d9dadb 45%, #8f8f8f 100%); }
  .brand { position: absolute; display: flex; align-items: center; gap: 5px; font-weight: 700; color: var(--navy); }
  .brand-mark { background: var(--green); display: inline-block; }
  .brand.small { left: 20px; top: 326px; font-size: 15px; }
  .brand.small .brand-mark { width: 11px; height: 11px; }

  .services { left: 465px; top: 0; width: 232px; height: 491px; }
  .services h2 { position: absolute; left: 28px; top: 42px; font-size: 15.5px; font-weight: 700; color: var(--navy); }
  .services ul { list-style: none; position: absolute; left: 28px; top: 93px; width: 178px; }
  .services li { height: 26.2px; font-size: 7.8px; line-height: 10px; border-bottom: 1px solid var(--rule); padding-top: 2px; white-space: nowrap; }
  .web-band { left: 466px; top: 491px; width: 231px; height: 50px; background: var(--green); color: #fff; font-weight: 700; font-style: italic; font-size: 9.3px; display: flex; align-items: center; justify-content: center; }

  /* outside spread */
  .files-photo { left: 0; top: 0; width: 235px; height: 205px; background: linear-gradient(160deg, #2f3d52 0%, #b8c2cc 45%, #eef1f4 70%, #7c8795 100%); }
  .pitch-title { left: 42px; top: 244px; font-size: 14.5px; line-height: 16px; font-weight: 700; color: var(--navy); }
  .pitch-body { left: 42px; top: 302px; width: 154px; font-size: 9.2px; line-height: 15.8px; text-align: justify; color: #5a5a5a; }
  .call-band { left: 0; top: 491px; width: 235px; height: 50px; background: var(--green); color: #fff; text-align: center; font-weight: 700; padding-top: 10px; }
  .call-band .call { font-size: 14.5px; line-height: 15px; display: block; }
  .call-band .free { font-size: 10px; line-height: 12px; display: block; }

  .quote { left: 267px; top: 77px; width: 161px; height: 83px; background: var(--quote-bg); padding: 10px 12px; font-style: italic; font-size: 6.9px; line-height: 10.4px; text-align: justify; color: #777; }
  .quote-tail { left: 362px; top: 160px; }
  .quote-name { left: 374px; top: 166px; font-style: italic; font-size: 7px; color: var(--navy); }
  .brand.mid { left: 284px; top: 250px; font-size: 26px; }
  .brand.mid .brand-mark { width: 18px; height: 18px; }
  .contact-band { left: 235px; top: 372px; width: 232px; height: 119px; background: var(--navy); color: #fff; font-size: 11px; line-height: 12.3px; padding: 28px 0 0 52px; }
  .contact-band p + p { margin-top: 11px; }
  .web-foot { left: 235px; top: 491px; width: 232px; height: 50px; background: var(--green); color: #fff; font-weight: 700; font-style: italic; font-size: 6px; display: flex; align-items: center; padding-left: 54px; }

  .doctor-photo { left: 467px; top: 0; width: 232px; height: 372px; background: linear-gradient(180deg, #f6f8f8 0%, #e5ecef 50%, #c6d3da 100%); }
  .brand.cover { left: 554px; top: 30px; font-size: 24px; }
  .brand.cover .brand-mark { width: 16px; height: 16px; }
  .cover-band { left: 467px; top: 372px; width: 232px; height: 119px; background: var(--navy); color: #fff; font-weight: 700; font-size: 19px; line-height: 17.8px; padding: 24px 0 0 32px; }
  .cover-foot { left: 467px; top: 491px; width: 232px; height: 50px; background: var(--green); color: #fff; font-size: 10.3px; line-height: 12px; padding: 12px 0 0 35px; }
</style>
</head>
<body>

<section class="sheet inside" aria-label="Brochure inside spread">
  <div class="block intro-panel">
    <h1 class="intro-title">THE BEST MEDICINE FOR A BROKEN BILLING CYCLE</h1>
    <h2 class="intro-sub">QUICK COST EFFECTIVE EFFICIENT BILLING SOLUTIONS</h2>
    <p class="intro-body">We do medical billing and consulting for all types of medical services including hospitals, clinics, physical therapy, mental health, and all other physician specialties.</p>
    <p class="intro-body right">Korvath Billing and Consulting offers 128 years of combined medical billing, coding, credentialing, auditing, and practice management experience. Integrity, reliability, dedication, and open communication are the cornerstones of our foundation. We strive to create meaningful relationships with our clients so they may focus on what they do best, and allow us to handle the rest.</p>
  </div>
  <p class="block notice-band">We understand the changes occurring in our healthcare system. Reimbursement is decreasing, expenses are increasing, and the dedication and tenacity to collect every dollar due from the carriers is vital to the financial health of the hospital or practitioner.</p>
  <div class="photo team-photo" role="img" aria-label="Photo of a smiling business team around a glass meeting table, giving thumbs up"></div>
  <div class="brand small"><span class="brand-mark"></span>Korvath</div>

  <div class="block services">
    <h2>SERVICES INCLUDE</h2>
    <ul>
      <li>ELECTRONIC &amp; PAPER CLAIMS</li>
      <li>INSURANCE FOLLOW UPS</li>
      <li>MONTHLY PATIENT BILLING</li>
      <li>PAYMENT POSTING</li>
      <li>COMPREHENSIVE MONTHLY REPORTS</li>
      <li>DENIAL MANAGEMENT INCLUDING APPEALS</li>
      <li>PAST DUE CLAIMS</li>
      <li>INSURANCE VERIFICATION</li>
      <li>AUTHORIZATION TRACKING</li>
      <li>PRACTICE CONSULTING</li>
      <li>REMOTE ACCESS CONSULTING</li>
      <li>TRACKING AND VERIFYING ALLOWABLES</li>
      <li>CREDENTIALING</li>
      <li>CLAIM CORRECTION AND RESUBMISSION</li>
      <li>EMERGENCY “FILL IN” OR TRANSITION BILLING-</li>
      <li>LET US WORK WHEN YOU CAN’T</li>
    </ul>
  </div>
  <div class="block web-band">www.korvathbilling.com</div>
</section>

<section class="sheet outside" aria-label="Brochure outside spread">
  <div class="photo files-photo" role="img" aria-label="Close-up photo of rows of medical record files"></div>
  <h2 class="block pitch-title">FEWER HEADACHES,<br>MORE PROFITABILITY</h2>
  <p class="block pitch-body">In this age of declining Reimbursement, there is no room for errors. Incorrect coding, can mean revenue that is lost forever. Stay in the Black with our professional billing services. The most competitive rates in the industry. We work in your system or ours. We have a clean claim rate of 98.7 percent and, we don’t get paid until YOU get paid.</p>
  <div class="block call-band"><span class="call">CALL 702-555-0147</span><span class="free">FOR A FREE CONSULTATION</span></div>

  <blockquote class="block quote">“On another note, I know I don’t say it often enough but Thank you both for all you are doing; your leadership, your patience, your professionalism and your kindness just to name a few. I appreciate you more than you know.”</blockquote>
  <svg class="block quote-tail" width="14" height="8" viewBox="0 0 14 8"><path d="M0 0 H14 L12 8 Z" fill="var(--quote-bg)"/></svg>
  <p class="block quote-name">T.L. Marsh</p>
  <div class="brand mid"><span class="brand-mark"></span>Korvath</div>
  <div class="block contact-band">
    <p>48 LARKSPUR RIDGE CT.<br>ALDER MESA, NM 88014</p>
    <p>TEL : 702.555.0147<br>FAX : 888.555.0192</p>
  </div>
  <div class="block web-foot">www.korvathbilling.com</div>

  <div class="photo doctor-photo" role="img" aria-label="Photo of a smiling female doctor with a stethoscope"></div>
  <div class="brand cover"><span class="brand-mark"></span>Korvath</div>
  <h1 class="block cover-band">THE BEST<br>MEDICINE FOR<br>A BROKEN<br>BILLING CYCLE</h1>
  <p class="block cover-foot">QUICK COST EFFECTIVE<br>EFFICIENT BILLING SOLUTIONS</p>
</section>

</body>
</html>
```